Publisher seeks book cover / Book cover for publishing house

Full cover (front, back and side of the book). 28 cm x 20 cm total (High 20 cm, width 13, side 2 cm) Front cover: Title of the author on top, centered (Mathieu Lacombe) Title: Charting the skies Subtitle: Working pilot aerial Bottom and centered: attached logo (Velmora Editions) in white, and edited eventualy. Side: From left to right: Editor logo (only "Velmora" word, without the "Editions" word, title and author name Back cover: Left text column ) Bottom: space available for the bar coded price and 2 or 3 lines of text Right text column (approx 6.5 cm wide) Bottom of the right colum, center of the right column: same attached logo (Velmora Editions) in white, and edited eventualy, with www.velmora-example.com below the logo. Left Lateral margin of the back cover, this book should be almost 1 cm)
Colors
Designer to choose colors to be used in the design.
Look and feel
Each slider illustrates characteristics of the customer's brand and the style your logo design should communicate.

```html
<!DOCTYPE html>
<html lang="fr">
<head>
<meta charset="utf-8">
<title>Charting the skies – couverture</title>
<link rel="stylesheet" href="https://fonts.googleapis.com/css2?family=Cinzel:wght@400&family=EB+Garamond:wght@400&family=Noto+Serif:wght@400;700&family=Arimo:wght@400&display=swap">
<style>
  :root {
    --back-blue: #7ea7d6;
    --white: #ffffff;
    --ink: #24303a;
    --sky-top: #8fc0ec;
    --sky-mid: #d9e8f2;
    --lagoon: #4fd2e3;
    --lagoon-pale: #a7ece8;
    --sand: #e9efdd;
  }
  * { margin: 0; padding: 0; box-sizing: border-box; }
  html, body { width: 1200px; height: 856px; overflow: hidden; background: #fff; }
  .cover { position: relative; width: 1200px; height: 856px; }

  .back-spine {
    position: absolute; left: 0; top: 0; width: 641px; height: 856px;
    background: var(--back-blue); color: var(--white);
  }
  .body-text {
    position: absolute; font-family: "EB Garamond", Georgia, serif;
    font-size: 14px; line-height: 17.2px; color: var(--white);
  }
  .body-text p { margin-bottom: 17px; }
  .bio { left: 29px; top: 31px; width: 236px; }
  .excerpt { left: 294px; top: 31px; width: 245px; }

  .price, .code {
    position: absolute; left: 29px; font-family: Arimo, Arial, sans-serif; color: var(--white);
  }
  .price { top: 542px; font-size: 24px; }
  .code { font-size: 20px; }
  .isbn { top: 615px; }
  .issn { top: 645px; }

  .publisher {
    position: absolute; font-family: "Noto Serif", Georgia, serif; font-weight: 700;
    color: var(--white); text-align: center; line-height: 1;
  }
  .publisher small { display: block; font-size: 0.5em; margin-bottom: 4px; }
  .publisher-back { left: 42px; top: 712px; width: 160px; font-size: 34px; }
  .website {
    position: absolute; left: 22px; top: 770px; width: 200px; text-align: center;
    font-family: "EB Garamond", Georgia, serif; font-size: 14px; color: var(--white);
  }

  .code-box { position: absolute; left: 278px; top: 686px; width: 179px; height: 105px; background: var(--white); }

  .spine-text {
    position: absolute; white-space: nowrap; color: var(--white);
    transform-origin: left top; transform: rotate(-90deg);
  }
  .spine-author { left: 588px; top: 239px; font-family: "Noto Serif", Georgia, serif; font-size: 22px; }
  .spine-title { left: 585px; top: 625px; font-family: Cinzel, Georgia, serif; font-size: 24px; letter-spacing: 1px; }
  .spine-publisher { left: 582px; top: 792px; font-family: "Noto Serif", Georgia, serif; font-weight: 700; font-size: 24px; }

  .front { position: absolute; left: 641px; top: 0; width: 559px; height: 856px; }
  .front-photo { position: absolute; inset: 0; width: 100%; height: 100%; }
  .front-author {
    position: absolute; left: 0; top: 52px; width: 100%; text-align: center;
    font-family: "Noto Serif", Georgia, serif; font-weight: 700; font-size: 42px;
    color: #f2f6ea; text-shadow: 1px 2px 3px rgba(40,60,60,.6);
  }
  .front-title {
    position: absolute; left: 0; top: 458px; width: 100%; text-align: center;
    font-family: Cinzel, Georgia, serif; font-size: 76px; line-height: 96px;
    color: var(--white); text-shadow: 1px 2px 4px rgba(60,80,90,.45);
  }
  .front-subtitle {
    position: absolute; left: 45px; top: 668px; width: 100%; text-align: center;
    font-family: "Noto Serif", Georgia, serif; font-size: 34px; color: var(--ink);
  }
  .publisher-front { left: 197px; top: 752px; width: 160px; font-size: 34px; }
</style>
</head>
<body>
<div class="cover">
  <section class="back-spine">
    <div class="body-text bio">
      <p>Pendant cinq ans, aux commandes de petits bimoteurs l'auteur a assuré le relais télévisé du Grand Tour cycliste, accompagnés des scientifiques en Polynésie, cartographié des régions entières.</p>
      <p>Il raconte ce métier méconnu, propice aux longs voyages. Aventure et autonomie sont au programme, entre vols à basse hauteur et convoyages, des îles Marquises au Nigeria, d'Abu Dhabi au Groenland, de l'Afrique du Sud au Canada.</p>
      <p>Par la suite, il a piloté un biréacteur Ciel 32 pour une compagnie africaine, avant de rejoindre Air Ciela où il est aujourd'hui copilote sur long courrier.</p>
    </div>
    <div class="body-text excerpt">
      <p>Je suis très sensible, pour l'avoir vécu souvent, à ce moment où la physionomie de l'environnement aérien change du tout au tout. En altitude, on flotte dans une clarté bleutée et un calme reposant. Dès que l'on quitte ce monde, en revanche, dès lors que l'on achève de se faufiler en descente entre les cumulus, dévalant trois mille mètres le long de ces nuages qui paraissaient si innocents et qui sont en fait des montagnes, on entre dans un tout autre ciel.</p>
      <p>Inconsciemment je courbe l'échine en glissant l'avion sous la base des cumulus. Je pousse alors la porte d'un monde plus secret, plus ténébreux, celui des petits avions besogneux dont le monde ignore l'existence. Mon jardin. Ici, les rayons de soleil sont filtrés par les montagnes d'eau en suspension au-dessus de la jungle. Au sortir de cette vapeur diaphane, la lumière n'en est que plus spectaculaire, elle fait pleuvoir dans notre ciel nouveau un éventail de faisceaux diagonaux griffant l'horizon.</p>
      <p>Vus d'en-dessous, les nuages ne sont plus les inoffensives boules blanches et bourgeonnantes que nous observions depuis notre altitude de croisière, mais une épaisse et menaçante masse sombre suspendue comme une épée de Damoclès au-dessus de nos têtes. Ils forment un couvercle hermétique au-dessus de l'Ouganda, une chape d'étain délimitant notre aire de jeu.</p>
    </div>
    <div class="price">15 euros</div>
    <div class="code isbn">ISBN 0000000</div>
    <div class="code issn">ISSN 0000000</div>
    <div class="publisher publisher-back"><small>Editions</small>VELMORA</div>
    <div class="website">www.velmora-example.com</div>
    <div class="code-box"></div>

    <div class="spine-text spine-author">Mathieu Lacombe</div>
    <div class="spine-text spine-title">CHARTING THE SKIES</div>
    <div class="spine-text spine-publisher">VELMORA</div>
  </section>

  <section class="front">
    <svg class="front-photo" role="img" aria-label="Photo : petit bimoteur survolant un lagon turquoise devant une île montagneuse" viewBox="0 0 559 856" preserveAspectRatio="none">
      <defs>
        <linearGradient id="lagoon-scene" x1="0" y1="0" x2="0" y2="1">
          <stop offset="0" stop-color="#8fc0ec"/>
          <stop offset="0.28" stop-color="#d9e8f2"/>
          <stop offset="0.32" stop-color="#5d8f6e"/>
          <stop offset="0.37" stop-color="#4fd2e3"/>
          <stop offset="0.6" stop-color="#a7ece8"/>
          <stop offset="1" stop-color="#e9efdd"/>
        </linearGradient>
      </defs>
      <rect width="559" height="856" fill="url(#lagoon-scene)"/>
    </svg>
    <div class="front-author">Mathieu Lacombe</div>
    <div class="front-title">CHARTING<br>THE SKIES</div>
    <div class="front-subtitle">Pilote de travail aérien</div>
    <div class="publisher publisher-front"><small>Editions</small>VELMORA</div>
  </section>
</div>
</body>
</html>
```